Roofing Company Modern look

I want a modern and sophisticated look for our roofing business.

Our address is :

4276 Pellman Crossing Rd
Cedarview, Fl 34719

(407)-583-2716

www.SummitcrestShinglesFl.com

I also want to make sure on the back there is a spot to put
Project Manager Name :

Number:

Because the cards will be used by all sales people

Project Manager Name :

Also there are accreditation we have logos are uploaded here as well that I would like maybe on the back of card as well

I also want to highlight our special attributions or trades:

Residential & Commercial
Fully Insured
License # CCC4872196
Insurance Claims
Serving Central Florida Since 1992
Free Estimates

Contact Information for Business Card

Our address is :

4276 Pellman Crossing Rd
Cedarview, Fl 34719

(407)-583-2716

Project Manager Name :

Residential & Commercial
Fully Insured
License # CCC4872196
Insurance Claims
Free Estimates

Font styles to use
Serif
Sans Serif

Colors
3176b5

Requirements
Must have
• Must have royal blue like my logo grey and black are the colors I like

```html
<!DOCTYPE html>
<html lang="en">
<head>
<meta charset="utf-8">
<title>Summitcrest Shingles & Gutters – Business Card</title>
<link href="https://fonts.googleapis.com/css2?family=Lato:wght@400;700&display=swap" rel="stylesheet">
<style>
  :root {
    --royal-blue: #3176b5;
    --ink-grey: #4a4a4a;
    --soft-grey: #5c5c5c;
    --paper: #ffffff;
    --backdrop: #2a2a2a;
  }
  * { margin: 0; padding: 0; box-sizing: border-box; }
  html, body {
    width: 1200px; height: 1192px; overflow: hidden;
    background: var(--backdrop);
    font-family: "Lato", sans-serif;
  }
  .card {
    position: absolute; left: 209px; width: 782px; height: 449px;
    border-radius: 12px; overflow: hidden;
  }
  .card--front { top: 130px; background: var(--paper); }
  .card--back { top: 614px; background: var(--royal-blue); }

  .brand {
    position: absolute; text-align: center; white-space: nowrap;
    font-weight: 700; line-height: 1.3;
  }
  .brand__mark { display: block; margin: 0 auto; border-radius: 50%; }
  .card--front .brand {
    left: 80px; width: 300px; top: 150px;
    color: var(--royal-blue); font-size: 17px; letter-spacing: 1.5px;
  }
  .card--front .brand__mark { width: 76px; height: 76px; background: var(--royal-blue); margin-bottom: 38px; }
  .card--back .brand {
    left: 0; width: 782px; top: 122px;
    color: var(--paper); font-size: 28px; letter-spacing: 3px;
  }
  .card--back .brand__mark { width: 100px; height: 100px; background: var(--paper); margin-bottom: 52px; }

  .divider {
    position: absolute; left: 390px; top: 111px; width: 2px; height: 225px;
    background: var(--royal-blue);
  }
  .contact { position: absolute; left: 409px; top: 108px; color: var(--soft-grey); }
  .contact__name { font-size: 25px; font-weight: 700; line-height: 28px; color: var(--ink-grey); }
  .contact__name .first { color: var(--royal-blue); }
  .contact__role { font-size: 19px; line-height: 22px; }
  .contact__line { font-size: 19px; line-height: 23px; }
  .contact__line .label { color: var(--royal-blue); }
  .gap-s { margin-top: 7px; }
  .rule { width: 11px; height: 2px; background: var(--royal-blue); margin: 5px 0 6px; }
  .icon-line { display: flex; align-items: center; gap: 8px; font-size: 19px; line-height: 23px; }
  .icon-line svg { width: 15px; height: 15px; fill: var(--royal-blue); flex: none; }

  .attributes {
    position: absolute; left: 0; width: 782px; top: 380px;
    display: flex; justify-content: center; align-items: center; gap: 10px;
    font-size: 17px; color: var(--soft-grey);
  }
  .attributes .dot { width: 8px; height: 8px; border-radius: 50%; background: var(--royal-blue); }

  .back-web {
    position: absolute; left: 0; width: 782px; top: 385px; text-align: center;
    color: var(--paper); font-size: 21px; letter-spacing: 0.5px;
  }
</style>
</head>
<body>
  <section class="card card--front">
    <div class="brand"><span class="brand__mark"></span>SUMMITCREST<br>SHINGLES &amp; GUTTERS INC.</div>
    <div class="divider"></div>
    <div class="contact">
      <div class="contact__name"><span class="first">Daniel</span> Harwick</div>
      <div class="contact__role">Project Manager</div>
      <div class="contact__line gap-s"><span class="label">License #</span> CCC4872196</div>
      <div class="contact__line">Residential &amp; Commercial</div>
      <div class="rule"></div>
      <div class="contact__line">4276 Pellman Crossing Rd</div>
      <div class="contact__line">Cedarview, Fl 34719</div>
      <div class="rule"></div>
      <div class="icon-line">
        <svg viewBox="0 0 24 24"><path d="M6.6 10.8a15 15 0 0 0 6.6 6.6l2.2-2.2c.3-.3.7-.4 1-.2 1.1.4 2.3.6 3.6.6.6 0 1 .4 1 1V20c0 .6-.4 1-1 1A17 17 0 0 1 3 4c0-.6.4-1 1-1h3.5c.6 0 1 .4 1 1 0 1.3.2 2.5.6 3.6.1.3 0 .7-.2 1z"/></svg>
        (407)-583-2716
      </div>
      <div class="icon-line">
        <svg viewBox="0 0 24 24"><path d="M2 5h20v2l-10 7L2 7z M2 9.5l10 7 10-7V19H2z"/></svg>
        SummitcrestShinglesFl@gmail.com
      </div>
      <div class="icon-line">
        <svg viewBox="0 0 24 24"><circle cx="12" cy="12" r="10"/></svg>
        www.SummitcrestShinglesFl.com
      </div>
    </div>
    <div class="attributes">
      <span>Fully Insured</span><span class="dot"></span>
      <span>Insurance Claims</span><span class="dot"></span>
      <span>Serving Central Florida Since 1992</span><span class="dot"></span>
      <span>Free Estimates</span>
    </div>
  </section>

  <section class="card card--back">
    <div class="brand"><span class="brand__mark"></span>SUMMITCREST<br>SHINGLES &amp; GUTTERS INC.</div>
    <div class="back-web">www.summitcrestshinglesfl.com</div>
  </section>
</body>
</html>
```